Landing page for a cyber security service provider called 'Lumen Grove'

The client is a new cyber security company in need of a website landing page at lumengrove.example.

Their visual identity is modern, playful, clean and uncluttered and represents innovation, connectivity and approachability.

The company logo is provided in black (attached) but the client is open to changing the colour to align with the new website design.

The landing page needs to contain:
- A call to action with a 'Get Started' button
-Links to blank 'How it works', 'Products', 'Pricing', 'About Us' and 'Contact Us' pages (that we'll fill out later)

Target Market(s)

Medium to large businesses who probably don't understand cyber / cyber security but need their business to be protected.

Industry/Entity Type

Cyber Security

Coding

Coded - Design and coding required

Number of Pages Required

1 page

Font styles to use
Sans Serif
Other font styles liked:
• Helvetica

Requirements
Nice to have
• Hero banner at the top of the landing page.
Should not have
• Should not look like a traditional cyber / cyber security design (eg no dark blue/ black, red/black colour combinations). Please no military styles (eg no shields, cannons, swords, guns)

```html
<!DOCTYPE html>
<html lang="en">
<head>
<meta charset="utf-8">
<title>Lumen Grove — Keep your business data safe</title>
<link href="https://fonts.googleapis.com/css2?family=Lilita+One&family=Inter:wght@400;500;600;700&display=swap" rel="stylesheet">
<style>
  :root{
    --pink:#f0259a;
    --pink-deep:#e81d8f;
    --orange:#f7a35c;
    --yellow:#fddc55;
    --ink:#222228;
    --muted:#4a4a55;
    --soft:#f6f7f9;
    --white:#ffffff;
    --line:#ececf0;
  }
  *{box-sizing:border-box;margin:0;padding:0}
  html,body{width:1200px;height:3579px;overflow:hidden;background:var(--white)}
  body{font-family:"Inter",Helvetica,Arial,sans-serif;color:var(--ink);position:relative}
  .abs{position:absolute}
  .display{font-family:"Lilita One","Arial Rounded MT Bold",sans-serif;font-weight:400}
  .grad-text{background:linear-gradient(90deg,var(--pink) 0%,var(--pink) 45%,var(--orange) 100%);-webkit-background-clip:text;background-clip:text;color:transparent}

  /* hero */
  .hero{left:0;top:0;width:1200px;height:688px;border-radius:0 0 48px 48px;overflow:hidden;
    background:linear-gradient(100deg,#ee3d9b 0%,#f27aa9 45%,#f29a9e 70%,#e8787f 100%)}
  .hero-photo{position:absolute;inset:0;background:radial-gradient(ellipse at 65% 40%,rgba(255,220,215,.55),transparent 55%),linear-gradient(90deg,rgba(236,40,150,.55),rgba(236,40,150,0) 60%)}
  .brand{left:130px;top:18px;width:60px;height:60px;border-radius:12px;background:var(--white);display:flex;align-items:center;justify-content:center;text-align:center;font-weight:700;font-size:11px;line-height:1.1;color:var(--pink)}
  .nav{right:130px;top:33px;display:flex;gap:6px}
  .nav a{display:block;background:var(--white);color:var(--pink);font-weight:700;font-size:12px;text-decoration:none;height:29px;line-height:29px;padding:0 12px;border-radius:15px}
  .hero-title{left:122px;top:322px;width:480px;font-size:39px;line-height:43px;color:var(--white);text-transform:uppercase;letter-spacing:.5px}
  .btn{display:flex;align-items:center;justify-content:center;gap:4px;background:var(--yellow);color:var(--ink);font-weight:700;text-decoration:none;border-radius:999px}
  .hero-btn{left:122px;top:492px;width:110px;height:34px;font-size:15px}

  /* shared section heads */
  .tag{background:var(--yellow);color:var(--pink);font-size:9px;font-weight:600;line-height:13px;padding:0 6px;border-radius:3px}
  .center-x{left:0;width:1200px;text-align:center}
  .head{font-size:35px;line-height:41px}
  .rule{height:4px;background:var(--pink);border-radius:2px}
  .body-text{font-size:14.5px;line-height:21.5px;color:var(--muted)}

  .media{border-radius:20px}
  .chips{display:flex;justify-content:center;gap:10px}
  .chip{display:flex;align-items:center;gap:6px;height:42px;padding:0 14px;border:1px solid var(--line);border-radius:10px;background:var(--white);font-size:12px;color:var(--ink);box-shadow:0 2px 6px rgba(0,0,0,.04)}
  .chip svg{width:12px;height:12px}

  /* safe-data card */
  .safe{left:136px;top:1706px;width:926px;height:325px;background:var(--soft);border-radius:28px}

  /* services */
  .service{width:292px;height:422px;background:var(--soft);border-radius:20px;overflow:hidden}
  .service-top{height:132px;background:radial-gradient(circle at 85% 20%,#ffe377 0,#fddc55 60%);padding:34px 34px 0}
  .service-top h3{font-size:20px;font-weight:700;margin-bottom:8px}
  .service-top p{font-size:11px;color:var(--muted);line-height:17px}
  .service-top .price{font-weight:700;color:var(--ink)}
  .service-img{position:absolute;left:34px;top:167px;width:223px;height:222px;border-radius:6px}

  /* cta */
  .cta{left:0;top:2981px;width:1200px;height:329px;background:linear-gradient(90deg,#ea1f92,#f02d9c 60%,#e81d8f)}
  .cta-title{left:163px;top:3080px;font-size:35px;line-height:42px;color:var(--white)}
  .cta-text{left:163px;top:3196px;width:400px;font-size:13px;line-height:21px;color:#ffe3f2}
  .cta-btn{left:754px;top:3117px;width:163px;height:56px;font-size:14px}

  /* footer */
  .foot-brand{left:140px;top:3378px;font-size:13px;font-weight:700;color:var(--ink)}
  .copy{left:136px;top:3440px;font-size:12px;color:var(--muted)}
  .foot-col h4{font-size:14px;font-weight:600;color:var(--pink);margin-bottom:6px}
  .foot-col a{display:block;font-size:11px;line-height:23px;color:var(--muted);text-decoration:none}
</style>
</head>
<body>

<!-- Hero -->
<header class="abs hero">
  <div class="hero-photo" role="img" aria-label="Woman in a light blazer typing at a desk beside server racks, tinted pink"></div>
</header>
<div class="abs brand">Lumen<br>Grove</div>
<nav class="abs nav">
  <a href="#">Home</a><a href="#">How it works</a><a href="#">Products</a><a href="#">Pricing</a><a href="#">About Us</a><a href="#">Contact Us</a>
</nav>
<h1 class="abs hero-title display">Business data is the most valuable. Losing it was a big disaster.</h1>
<a class="abs btn hero-btn" href="#">Solution
  <svg width="13" height="13" viewBox="0 0 14 14"><path d="M1 7h11M8 3l4 4-4 4" stroke="#222228" stroke-width="2" fill="none" stroke-linecap="round"/></svg></a>

<!-- Asset -->
<div class="abs" style="left:574px;top:794px"><span class="tag">important</span></div>
<h2 class="abs center-x head display" style="top:806px"><span class="grad-text">The most important asset.</span></h2>
<div class="abs rule" style="left:553px;top:862px;width:94px"></div>
<p class="abs body-text" style="left:326px;top:890px;width:548px;text-align:center">Digital data is the most important asset for modern businesses. With accurate data, you can make informed decisions, enhance operational efficiency, and strengthen customer relationships.</p>
<div class="abs media" style="left:320px;top:978px;width:560px;height:320px;background:linear-gradient(120deg,#b2328f,#e6a3cf 45%,#c94a9f 100%)" role="img" aria-label="Desktop computer showing a data table on a pink-lit desk"></div>

<!-- Causes -->
<div class="abs" style="left:587px;top:1404px"><span class="tag">lost</span></div>
<h2 class="abs center-x head display" style="top:1414px"><span class="grad-text">Causes of data loss.</span></h2>
<div class="abs rule" style="left:563px;top:1469px;width:74px"></div>
<div class="abs center-x chips" style="top:1500px">
  <div class="chip"><svg viewBox="0 0 12 12"><circle cx="6" cy="6" r="5.5" fill="#222228"/><circle cx="4" cy="5" r="1" fill="#fff"/><circle cx="8" cy="5" r="1" fill="#fff"/></svg>Human error</div>
  <div class="chip"><svg viewBox="0 0 12 12"><circle cx="6" cy="6" r="3.5" fill="#222228"/><path d="M6 0v3M6 9v3M0 6h3M9 6h3M2 2l2 2M8 8l2 2M10 2 8 4M2 10l2-2" stroke="#222228" stroke-width="1.3"/></svg>Failure system</div>
  <div class="chip"><svg viewBox="0 0 12 12"><rect x="2" y="5" width="8" height="7" rx="1" fill="#222228"/><circle cx="6" cy="3" r="2.5" fill="#222228"/></svg>Hacker attacks</div>
</div>
<p class="abs center-x body-text" style="top:1569px">It can cause chaos within your company. This is a big disaster that cannot be ignored.</p>

<!-- Safe data -->
<section class="abs safe"></section>
<div class="abs" style="left:171px;top:1741px"><span class="tag">safe-data</span></div>
<h2 class="abs head display" style="left:171px;top:1752px;width:360px"><span class="grad-text">Keep safe your business data.</span></h2>
<div class="abs rule" style="left:171px;top:1849px;width:66px"></div>
<p class="abs body-text" style="left:171px;top:1879px;width:400px;font-size:13.5px">We offer a robust cybersecurity solution to keep your valuable data safe. With reliable backup systems and top-tier cybersecurity, your data will be protected from potential hacker attacks and other threats. We ensure your business stays clear of big disasters.</p>
<div class="abs" style="left:635px;top:1754px;width:394px;height:225px;border-radius:10px;background:linear-gradient(110deg,#e9b3b5,#f3d3cf 50%,#d99ea3)" role="img" aria-label="Smiling businesswoman working on a laptop at a desk with plants"></div>

<!-- Services -->
<div class="abs" style="left:576px;top:2102px"><span class="tag">services</span></div>
<h2 class="abs center-x head display" style="top:2113px"><span class="grad-text">The best service for your<br>data security.</span></h2>
<div class="abs rule" style="left:561px;top:2211px;width:78px"></div>

<article class="abs service" style="left:140px;top:2250px">
  <div class="service-top"><h3>Service One</h3><p>lorem ipsum dolores<br><span class="price">$ 45</span></p></div>
  <div class="service-img" style="background:linear-gradient(135deg,#2a2f45,#d9579d 50%,#3a2a40)" role="img" aria-label="Computer workstation in a server room"></div>
</article>
<article class="abs service" style="left:454px;top:2250px">
  <div class="service-top"><h3>Service Two</h3><p>lorem ipsum dolores<br><span class="price">$ 50</span></p></div>
  <div class="service-img" style="background:linear-gradient(135deg,#c65a8e,#f2c4d8 50%,#b8456f)" role="img" aria-label="Isometric server rack on a platform"></div>
</article>
<article class="abs service" style="left:768px;top:2250px">
  <div class="service-top"><h3>Service Three</h3><p>lorem ipsum dolores<br><span class="price">$ 70</span></p></div>
  <div class="service-img" style="background:linear-gradient(135deg,#e9a4c0,#f6d4df 50%,#c06a9a)" role="img" aria-label="Isometric cloud data center illustration"></div>
</article>

<!-- Support -->
<div class="abs" style="left:581px;top:2757px"><span class="tag">support</span></div>
<h2 class="abs center-x head display" style="top:2768px"><span class="grad-text">Our support.</span></h2>
<div class="abs rule" style="left:562px;top:2823px;width:76px"></div>
<div class="abs center-x chips" style="top:2856px">
  <div class="chip"><svg viewBox="0 0 12 12"><path d="M2 7V6a4 4 0 0 1 8 0v1" stroke="#222228" stroke-width="1.5" fill="none"/><rect x="1" y="6" width="3" height="4" rx="1" fill="#222228"/><rect x="8" y="6" width="3" height="4" rx="1" fill="#222228"/></svg>Support One</div>
  <div class="chip"><svg viewBox="0 0 12 12"><rect x="0" y="3" width="12" height="7" rx="3" fill="#222228"/><circle cx="4" cy="6.5" r="1" fill="#fff"/><circle cx="8" cy="6.5" r="1" fill="#fff"/></svg>Support Two</div>
  <div class="chip"><svg viewBox="0 0 12 12"><rect x="0" y="5" width="3" height="7" fill="#222228"/><path d="M4 5l3-5c1 0 2 1 1.5 2.5L8 5h3c1 0 1 1 1 1l-1 5c0 1-1 1-1 1H4z" fill="#222228"/></svg>Support Three</div>
  <div class="chip"><svg viewBox="0 0 12 12"><rect x="0" y="1" width="12" height="4" rx="1" fill="#222228"/><rect x="0" y="7" width="12" height="4" rx="1" fill="#222228"/></svg>Support Four</div>
</div>

<!-- CTA -->
<section class="abs cta" role="img" aria-label="Magenta band with a faint circuit board texture"></section>
<div class="abs" style="left:163px;top:3052px"><span class="tag">protect-data</span></div>
<h2 class="abs cta-title display">Protect your business<br>data properly.</h2>
<div class="abs rule" style="left:163px;top:3159px;width:66px;background:var(--yellow)"></div>
<p class="abs cta-text">Don't let disaster strike your company. Protect your most valuable data. Click the get started button.</p>
<a class="abs btn cta-btn" href="#">Get Started
  <svg width="13" height="13" viewBox="0 0 14 14"><path d="M1 7h11M8 3l4 4-4 4" stroke="#222228" stroke-width="2" fill="none" stroke-linecap="round"/></svg></a>

<!-- Footer -->
<div class="abs foot-brand">Lumen Grove</div>
<p class="abs copy">© 2024</p>
<div class="abs foot-col" style="left:514px;top:3380px"><h4>Section</h4><a href="#">Home</a><a href="#">Features</a><a href="#">Pricing</a><a href="#">FAQs</a><a href="#">About</a></div>
<div class="abs foot-col" style="left:703px;top:3380px"><h4>Section</h4><a href="#">Home</a><a href="#">Features</a><a href="#">Pricing</a><a href="#">FAQs</a><a href="#">About</a></div>
<div class="abs foot-col" style="left:892px;top:3380px"><h4>Section</h4><a href="#">Home</a><a href="#">Features</a><a href="#">Pricing</a><a href="#">FAQs</a><a href="#">About</a></div>

</body>
</html>
```